Bref créative
QVEN
Maple Growth Allies for Youth
I need single sided standard sized Business Card [3.5" x 2"]
Use the Logo font or others - Open to ideas....
Professional
Marissa Holden, M.S., CCC/SLP
Owner of SproutWell Therapy
4816 Fenwick Parkway, Suite 215
Dallas, Texas 75219
mholden@sproutwelltherapy.example
www.qven.example
Looking for professional and clean.

```html
<!DOCTYPE html>
<html lang="en">
<head>
<meta charset="utf-8">
<title>QVEN Stationery Set</title>
<link href="https://fonts.googleapis.com/css2?family=Nunito:wght@400;800&display=swap" rel="stylesheet">
<style>
  :root{
    --bg:#2e2f31;
    --paper:#ffffff;
    --navy:#2c3992;
    --red:#e1232b;
    --ink:#3a3d55;
    --faint:#e6e8f2;
    --caption:#9a9ca3;
  }
  *{margin:0;padding:0;box-sizing:border-box}
  html,body{width:1200px;height:336px;overflow:hidden;background:var(--bg);font-family:"Nunito",Arial,sans-serif}
  .canvas{position:relative;width:1200px;height:336px}
  .item{position:absolute;background:var(--paper);overflow:hidden;box-shadow:0 2px 6px rgba(0,0,0,.5)}
  .item svg.bg{position:absolute;inset:0;width:100%;height:100%}
  .brand{position:absolute;font-weight:800;color:var(--navy);letter-spacing:.5px;line-height:1;display:flex;align-items:center;gap:3px}
  .brand .dot{display:inline-block;border-radius:50%;background:var(--red)}
  .tagline{position:absolute;color:var(--navy);font-size:3.5px;white-space:nowrap}
  .watermark{position:absolute;font-weight:800;color:var(--faint);line-height:1}
  .details{position:absolute;color:var(--ink);font-size:4px;line-height:1.45;white-space:nowrap}
  .details strong{color:var(--navy);font-weight:800;font-size:5px}
  .caption{position:absolute;color:var(--caption);font-size:5px;white-space:nowrap}
  .primary-logo{position:absolute;left:14px;top:30px}
</style>
</head>
<body>
<div class="canvas">

  <!-- primary logo -->
  <div class="brand primary-logo" style="font-size:30px"><span class="dot" style="width:8px;height:8px"></span>QVEN</div>
  <div class="tagline" style="left:30px;top:66px;color:#c9cce0;font-size:5px">Maple Growth Allies for Youth</div>
  <div class="caption" style="left:30px;top:108px">Primary Logo</div>

  <!-- business card front -->
  <div class="item card-front" style="left:19px;top:156px;width:120px;height:62px">
    <svg class="bg" viewBox="0 0 120 62" preserveAspectRatio="none">
      <path d="M0 0 H22 Q10 31 20 62 H0 Z" fill="var(--navy)"/>
      <path d="M22 0 Q10 31 20 62 H23 Q13 31 25 0 Z" fill="var(--red)"/>
    </svg>
    <div class="details" style="left:36px;top:8px"><strong>Marissa Holden</strong><br>M.S., CCC/SLP<br>Owner of SproutWell Therapy<br>4816 Fenwick Parkway, Suite 215<br>Dallas, Texas 75219<br>mholden@sproutwelltherapy.example<br>www.qven.example</div>
  </div>
  <div class="caption" style="left:30px;top:222px">Card Front</div>

  <!-- business card back -->
  <div class="item card-back" style="left:19px;top:240px;width:120px;height:62px">
    <svg class="bg" viewBox="0 0 120 62" preserveAspectRatio="none">
      <path d="M0 0 H18 Q8 31 16 62 H0 Z" fill="var(--navy)"/>
    </svg>
    <div class="brand" style="left:40px;top:20px;font-size:17px"><span class="dot" style="width:5px;height:5px"></span>QVEN</div>
    <div class="tagline" style="left:40px;top:40px">Maple Growth Allies for Youth</div>
  </div>
  <div class="caption" style="left:30px;top:306px">Card Back</div>

  <!-- letterhead page one -->
  <div class="item letterhead" style="left:173px;top:14px;width:211px;height:293px">
    <svg class="bg" viewBox="0 0 211 293" preserveAspectRatio="none">
      <path d="M0 0 H12 Q2 40 6 110 L0 120 Z" fill="var(--navy)"/>
      <path d="M0 268 Q70 250 120 272 T211 262 V293 H0 Z" fill="var(--navy)"/>
      <path d="M0 266 Q70 248 120 270 T211 260 V262 Q160 276 120 274 T0 269 Z" fill="var(--red)"/>
    </svg>
    <div class="brand" style="left:20px;top:12px;font-size:19px"><span class="dot" style="width:5px;height:5px"></span>QVEN</div>
    <div class="tagline" style="left:28px;top:33px">Maple Growth Allies for Youth</div>
    <div class="details" style="left:120px;top:12px;font-size:3.5px">4816 Fenwick Parkway, Suite 215<br>Dallas, Texas 75219<br>mholden@sproutwelltherapy.example<br>www.qven.example</div>
    <div class="watermark" style="left:48px;top:120px;font-size:44px">QVEN</div>
  </div>
  <div class="caption" style="left:250px;top:310px">Letterhead</div>

  <!-- letterhead page two -->
  <div class="item letterhead-second" style="left:403px;top:14px;width:216px;height:293px">
    <svg class="bg" viewBox="0 0 216 293" preserveAspectRatio="none">
      <path d="M0 276 Q80 262 130 280 T216 272 V293 H0 Z" fill="var(--navy)"/>
      <path d="M0 274 Q80 260 130 278 T216 270 V272 Q170 284 130 282 T0 277 Z" fill="var(--red)"/>
    </svg>
    <div class="brand" style="left:76px;top:16px;font-size:22px"><span class="dot" style="width:6px;height:6px"></span>QVEN</div>
    <div class="tagline" style="left:82px;top:40px">Maple Growth Allies for Youth</div>
    <div class="watermark" style="left:52px;top:122px;font-size:44px">QVEN</div>
  </div>
  <div class="caption" style="left:485px;top:310px">Second Page</div>

  <!-- envelope front -->
  <div class="item envelope-front" style="left:636px;top:209px;width:233px;height:91px">
    <svg class="bg" viewBox="0 0 233 91" preserveAspectRatio="none">
      <path d="M0 78 Q90 66 150 82 T233 74 V91 H0 Z" fill="var(--navy)"/>
      <path d="M0 76 Q90 64 150 80 T233 72 V74 Q190 86 150 84 T0 79 Z" fill="var(--red)"/>
    </svg>
    <div class="brand" style="left:10px;top:8px;font-size:14px"><span class="dot" style="width:4px;height:4px"></span>QVEN</div>
    <div class="details" style="left:12px;top:25px;font-size:3.2px">4816 Fenwick Parkway, Suite 215<br>Dallas, Texas 75219</div>
  </div>
  <div class="caption" style="left:720px;top:304px">Envelope Front</div>

  <!-- envelope back, red flap -->
  <div class="item envelope-red" style="left:876px;top:14px;width:300px;height:104px">
    <svg class="bg" viewBox="0 0 300 104" preserveAspectRatio="none">
      <path d="M0 0 H300 V22 L150 48 L0 22 Z" fill="var(--red)"/>
      <path d="M0 104 L150 60 L300 104" fill="none" stroke="#e2e3e8" stroke-width="1"/>
    </svg>
    <div class="brand" style="left:124px;top:52px;font-size:18px"><span class="dot" style="width:5px;height:5px"></span>QVEN</div>
  </div>

  <!-- envelope back, navy flap -->
  <div class="item envelope-navy" style="left:876px;top:124px;width:300px;height:92px">
    <svg class="bg" viewBox="0 0 300 92" preserveAspectRatio="none">
      <path d="M0 0 H300 V18 L150 44 L0 18 Z" fill="var(--navy)"/>
      <path d="M0 92 L150 54 L300 92" fill="none" stroke="#e2e3e8" stroke-width="1"/>
    </svg>
  </div>

  <!-- envelope back, plain -->
  <div class="item envelope-plain" style="left:876px;top:221px;width:300px;height:96px">
    <svg class="bg" viewBox="0 0 300 96" preserveAspectRatio="none">
      <path d="M0 0 L150 46 L300 0" fill="none" stroke="#cfd1d8" stroke-width="1"/>
      <path d="M0 96 L130 46 M300 96 L170 46" fill="none" stroke="#dcdde3" stroke-width="1"/>
    </svg>
  </div>
  <div class="caption" style="left:1000px;top:322px">Envelope Back</div>

</div>
</body>
</html>
```